CarePulse website blog. Simple medical advice given in clear yes or no answers that save people money

I am developing a new web page that provides medical care cost savings at the consumers' fingertips. I need a web page that is clean, concise, and attractive for me to put my valuable medical information on. The information I provide is simple to obtain, yet very valuable to the consumer, and answered in a yes or no format. For example, A person may wonder if they need an antibiotic for cold like symptoms. Seeing a doctor for an antibiotic is very expensive. But with simple and clear advice at their fingertips, they can confidently avoid having to pay $200 or more to see a doctor and get an antibiotic. This is kind of like consumer reports for medical services.

Target Market(s)

People who are savvy shoppers and want to save money on healthcare. Likely younger ages between 21 and 60, who are mobile, readily use iphones, and want strong evidence based research to guide their decisions.

Industry/Entity Type

Lifestyle

Coding

Number of Pages Required

Colors

Designer to choose colors to be used in the design.

Requirements
Must have
• A template on the "Question" and "Answer" page that can be edited many times that can be edited many times. The Confidence rating scale would need to be edited as well. The "Date Researched" the "CarePulse Caressage" and "References" all need to be able to be edited. This website must be very clear and simple to understand. A medical question is posed with a yes or no answer, then answered and given a confidence rating, we then tell them how much money they saved by going to our website.
Nice to have
• We want this to be slightly fun, vibrant, warm and inviting. This will be sometime later converted into an app format. Quirky, some humor to keep it interesting.
Should not have
• No sterile looking medical images. Not boring.

```html
<!DOCTYPE html>
<html lang="en">
<head>
<meta charset="utf-8">
<title>CarePulse — Clear. Valuable. Health.</title>
<link href="https://fonts.googleapis.com/css2?family=Montserrat:wght@400;500;600&family=Nunito:wght@700;800;900&display=swap" rel="stylesheet">
<style>
  :root{
    --blue:#1272bb;
    --blue-dark:#0d5c9a;
    --red:#e8232b;
    --ink:#1d1d1d;
    --grey-tab:#a3a3a3;
    --footer:#3b3b3b;
    --line:#e2e2e2;
    --white:#ffffff;
  }
  *{box-sizing:border-box;margin:0;padding:0}
  html,body{width:1200px;height:1033px;overflow:hidden;background:var(--white)}
  body{position:relative;font-family:"Montserrat",sans-serif;color:var(--ink)}

  .brand{position:absolute;left:111px;top:30px;display:flex;align-items:center;gap:12px}
  .brand-dot{width:46px;height:46px;border-radius:50%;background:var(--blue)}
  .brand-name{font-family:"Nunito",sans-serif;font-weight:900;font-size:34px;color:var(--red)}

  .search{position:absolute;left:386px;top:51px;width:305px;height:43px;border:2px solid #d7d7d7;border-radius:22px;display:flex;align-items:center;overflow:hidden}
  .search-field{flex:1;padding-left:15px;font-size:13.5px;color:#666}
  .search-btn{width:110px;height:43px;margin-right:-2px;background:var(--blue);color:var(--white);border-radius:22px;display:flex;align-items:center;justify-content:center;font-size:14.5px;font-weight:500}

  .tagline-band{position:absolute;left:0;top:0;width:1200px;height:136px}
  .tagline{position:absolute;left:736px;top:36px;width:370px;text-align:center;font-family:"Nunito",sans-serif;font-weight:900;font-size:24px;line-height:31px;letter-spacing:1.5px;color:var(--white)}

  .rule{position:absolute;left:111px;top:159px;width:978px;height:2px;background:var(--line)}
  .nav{position:absolute;left:111px;top:180px;width:978px;display:flex;justify-content:space-between;font-size:15.5px;font-weight:500}

  .hero{position:absolute;left:0;top:219px;width:1200px;height:559px;background:radial-gradient(ellipse at 45% 45%,#6a9ccd 0%,#4f88c1 50%,#3f78b4 100%)}
  .side-menu{position:absolute;left:0;top:102px;list-style:none}
  .side-item{width:289px;height:54px;margin-bottom:6px;background:var(--white);border-radius:0 27px 27px 0;display:flex;align-items:center;font-size:16.5px;font-weight:500}
  .side-icon{width:44px;height:46px;margin:0 16px 0 4px;display:flex;align-items:center;justify-content:center}
  .side-icon.blue{background:var(--blue)}
  .side-icon.red{background:var(--red)}
  .side-icon svg{width:24px;height:24px;fill:none;stroke:var(--white);stroke-width:1.8;stroke-linecap:round;stroke-linejoin:round}

  .hero-copy{position:absolute;left:334px;top:127px;width:300px;text-align:center;font-family:"Nunito",sans-serif;font-weight:800;font-size:36px;line-height:50px;color:var(--white)}
  .hero-cta{position:absolute;left:414px;top:350px;width:141px;height:45px;border:2.5px solid var(--white);border-radius:23px;display:flex;align-items:center;justify-content:center;color:var(--white);font-size:17px;font-weight:500}
  .dots{position:absolute;left:454px;top:424px;display:flex;gap:5px}
  .dots span{width:16px;height:16px;border-radius:50%;background:rgba(255,255,255,.55)}
  .dots span:first-child{background:var(--white)}
  .hero-art{position:absolute;left:754px;top:38px;width:335px;height:480px;border-radius:20px;background:linear-gradient(160deg,#3d5fc8 0%,#2c49a8 55%,#6f8fd6 100%);opacity:.85}

  .join-tab{position:absolute;left:377px;top:780px;width:446px;height:69px}
  .join-title{position:absolute;left:377px;top:798px;width:446px;text-align:center;font-family:"Nunito",sans-serif;font-weight:800;font-size:26px;color:var(--white)}

  .signup{position:absolute;left:291px;top:874px;display:flex;gap:9px}
  .email-field{width:493px;height:44px;border:2px solid #d7d7d7;border-radius:22px;padding-left:17px;display:flex;align-items:center;font-size:14.5px;color:#666}
  .submit-btn{width:117px;height:44px;border-radius:22px;background:var(--blue);color:var(--white);display:flex;align-items:center;justify-content:center;font-size:15.5px;font-weight:500}

  .footer{position:absolute;left:0;top:958px;width:1200px;height:75px;background:var(--footer);color:var(--white);font-family:"Nunito",sans-serif;font-weight:700}
  .legal{position:absolute;left:111px;top:13px;font-size:15.5px;line-height:28px}
  .ask{position:absolute;right:111px;top:11px;text-align:right;font-size:19px;line-height:28px}
  .ask a{color:var(--white);text-decoration:underline}
</style>
</head>
<body>

<svg class="tagline-band" viewBox="0 0 1200 136" aria-hidden="true">
  <path d="M668 0 Q720 30 725 80 Q728 128 770 133 L1200 133 L1200 136 L768 136 Q722 130 720 82 Q716 32 662 0 Z" fill="var(--red)"/>
  <path d="M668 0 Q720 30 725 80 Q728 128 770 131 L1200 131 L1200 0 Z" fill="var(--blue)"/>
</svg>
<div class="tagline">CLEAR. VALUABLE. HEALTH.<br>ADVICE. RIGHT NOW.</div>

<div class="brand"><span class="brand-dot"></span><span class="brand-name">CarePulse</span></div>

<div class="search"><span class="search-field">Search Here...</span><span class="search-btn">Search</span></div>

<div class="rule"></div>
<nav class="nav">
  <span>Prev / Screening</span><span>Women's Health</span><span>Men's Health</span><span>Meds</span><span>Surgery</span><span>Imaging</span><span>Peds</span><span>Contact Us</span>
</nav>

<section class="hero">
  <ul class="side-menu">
    <li class="side-item"><span class="side-icon blue"><svg viewBox="0 0 24 24"><circle cx="12" cy="12" r="9"/><path d="M9.5 9.5a2.5 2.5 0 1 1 3.5 2.3c-.7.3-1 .8-1 1.5v.5"/><circle cx="12" cy="17" r=".4"/></svg></span>Who Are We?</li>
    <li class="side-item"><span class="side-icon red"><svg viewBox="0 0 24 24"><path d="M12 4 3 8.5 12 13l9-4.5z"/><path d="M3 12.5 12 17l9-4.5"/><path d="M3 16.5 12 21l9-4.5"/></svg></span>How It Works?</li>
    <li class="side-item"><span class="side-icon blue"><svg viewBox="0 0 24 24"><path d="M3 5h6a3 3 0 0 1 3 3v12a2 2 0 0 0-2-2H3z"/><path d="M21 5h-6a3 3 0 0 0-3 3v12a2 2 0 0 1 2-2h7z"/></svg></span>Evidence Based Research</li>
    <li class="side-item"><span class="side-icon red"><svg viewBox="0 0 24 24"><circle cx="12" cy="8" r="4"/><path d="M4 21c0-4.4 3.6-7 8-7s8 2.6 8 7"/><path d="M12 16v3M10.5 17.5h3"/></svg></span>Dr. Whitmore</li>
    <li class="side-item"><span class="side-icon blue"><svg viewBox="0 0 24 24"><circle cx="12" cy="7" r="3.5"/><path d="M4 21c0-4.4 3.6-8 8-8s8 3.6 8 8z"/></svg></span>Who We Are Not</li>
    <li class="side-item"><span class="side-icon red"><svg viewBox="0 0 24 24"><path d="M12 3v18M7 21h10M4 6h16"/><path d="M6 6 3 13h6zM18 6l-3 7h6z"/></svg></span>Are We Biased?</li>
  </ul>

  <h1 class="hero-copy">Save $1,000 per Year On Healthcare. It's Free!</h1>
  <div class="hero-cta">Click Here!</div>
  <div class="dots"><span></span><span></span><span></span></div>

  <div class="hero-art" role="img" aria-label="Illustration of a woman holding a phone beside a large smartphone showing a doctor, with a plant, pills and a stethoscope"></div>
</section>

<svg class="join-tab" viewBox="0 0 446 69" aria-hidden="true">
  <path d="M0 0 H446 Q420 4 414 40 Q410 69 380 69 H66 Q36 69 32 40 Q26 4 0 0 Z" fill="var(--grey-tab)"/>
</svg>
<div class="join-title">Become A CarePulse Today!</div>

<div class="signup"><span class="email-field">Enter Email</span><span class="submit-btn">Submit</span></div>

<footer class="footer">
  <p class="legal">Copyrights @ 2018 CarePulse. All Rights Reserved.<br>Disclaimer: Nemo enim ipsam voluptatem quia voluptas quae ab illo inventore</p>
  <p class="ask">Ask a question here!<br><a>If it is worthy, Well post it!</a></p>
</footer>

</body>
</html>
```